Water ATM Card

Need a design for water ATM cards. Size of card is 3.375 x 2.125 inch
On the Front include the Cedar Brook Logo.
Bottom right corner should have Price $100
On the Back
This card is to be used to access water refills at any Cedar Brook Water Vending Machines.
Please contact (869) 415 2983 or (869) 238 4617 or email clearflowhub@mailbox-example.com for any assistance or recharging of card.

```html
<!DOCTYPE html>
<html lang="en">
<head>
<meta charset="utf-8">
<title>Cedar Brook Water ATM Card</title>
<link rel="stylesheet" href="https://fonts.googleapis.com/css2?family=Montserrat:wght@600;700&family=Lato:wght@300;400;700;900&family=Dancing+Script:wght@600&display=swap">
<style>
  :root {
    --backdrop: #bdbdbd;
    --label-grey: #5f5f5f;
    --card-white: #ffffff;
    --brand-blue: #0b6fba;
    --tag-blue: #1f5ea8;
    --soft-green: #7cc26f;
    --deep-navy: #2b3990;
    --back-navy: #283891;
  }
  * { box-sizing: border-box; margin: 0; padding: 0; }
  html, body {
    width: 1200px; height: 1000px; overflow: hidden;
    background: var(--backdrop);
    font-family: "Lato", Arial, sans-serif;
  }
  .canvas { position: relative; width: 1200px; height: 1000px; }

  .side-label {
    position: absolute; left: 262px;
    transform: translate(-50%, -50%) rotate(-90deg);
    font-family: "Lato", Arial, sans-serif; font-weight: 300;
    font-size: 25px; letter-spacing: 7px; color: var(--label-grey);
    white-space: nowrap;
  }
  .side-label--front { top: 318px; }
  .side-label--back { top: 710px; }

  .card {
    position: absolute; left: 347px; width: 506px; height: 319px;
    border-radius: 22px; overflow: hidden; background: var(--card-white);
    box-shadow: 0 3px 8px rgba(0,0,0,0.28);
  }
  .card--front { top: 158px; }
  .card--back { top: 551px; }
  .card svg.art { position: absolute; inset: 0; width: 506px; height: 319px; }

  .brand-name {
    position: absolute; left: 0; right: 0; text-align: center;
    font-family: "Montserrat", Arial, sans-serif; font-weight: 700;
    color: var(--brand-blue); letter-spacing: 0.5px;
  }
  .card--front .brand-name { top: 112px; font-size: 26px; }
  .tagline {
    position: absolute; left: 0; right: 0; top: 142px; text-align: center;
    font-family: "Montserrat", Arial, sans-serif; font-weight: 600;
    font-size: 16px; color: var(--tag-blue);
  }
  .price {
    position: absolute; right: 36px; top: 258px;
    color: var(--card-white); display: flex; align-items: center; gap: 2px;
  }
  .price__label {
    font-family: "Dancing Script", cursive; font-size: 18px;
    transform: rotate(-68deg); display: inline-block;
  }
  .price__amount { font-family: "Lato", Arial, sans-serif; font-weight: 900; font-size: 42px; line-height: 1; }

  .card--back .brand-name { top: 50px; font-size: 36px; }
  .usage-note {
    position: absolute; left: 0; right: 0; top: 201px; text-align: center;
    color: var(--card-white); font-size: 14px; line-height: 20px;
  }
  .usage-note strong { font-weight: 700; }
</style>
</head>
<body>
<div class="canvas">
  <div class="side-label side-label--front">FRONT</div>
  <div class="side-label side-label--back">BACK</div>

  <section class="card card--front" aria-label="Card front">
    <svg class="art" viewBox="0 0 506 319" role="img" aria-label="Decorative water wave graphic along the lower edge">
      <defs>
        <linearGradient id="wave-fill" x1="0" y1="1" x2="1" y2="0">
          <stop offset="0" stop-color="var(--brand-blue)"/>
          <stop offset="0.7" stop-color="var(--brand-blue)"/>
          <stop offset="1" stop-color="var(--deep-navy)"/>
        </linearGradient>
      </defs>
      <path d="M0,300 C160,296 330,190 506,200 L506,319 L0,319Z" fill="url(#wave-fill)"/>
    </svg>
    <div class="brand-name">CEDAR BROOK</div>
    <div class="tagline">Purified Spring Water</div>
    <div class="price"><span class="price__label">Price</span><span class="price__amount">$100</span></div>
  </section>

  <section class="card card--back" aria-label="Card back">
    <svg class="art" viewBox="0 0 506 319" aria-hidden="true">
      <path d="M0,132 C120,168 210,176 300,164 C380,154 440,150 506,172 L506,319 L0,319Z" fill="var(--back-navy)"/>
    </svg>
    <div class="brand-name">CEDAR BROOK</div>
    <p class="usage-note">
      <strong>This card is to be used to access water refills at any<br>
      Cedar Brook Water Vending Machines.</strong><br>
      Please contact <strong>(869) 415 2983</strong> or <strong>(869) 238 4617</strong> or email<br>
      <strong>clearflowhub@mailbox-example.com</strong> for any assistance or recharging of card.
    </p>
  </section>
</div>
</body>
</html>
```